New counselling and hypnotherapy business

I'd like a flyer which is relevant to people who want support and to improve their wellbeing which follows the same theme as my website: http://larkmoretherapy.plumweave.com
And emphasise that whatever the area of concern, development or growth and I can tailor my knowledge and skills to help.

I'd like to use the same logo and my emphasis is to draw the audience in...therapy and counselling is for people who are "stuck" and having a difficult time...it can also be useful has a personal development tool.

Hypnotherapy

```html
<!DOCTYPE html>
<html lang="en">
<head>
<meta charset="utf-8">
<title>Larkmore Counselling &amp; Hypnotherapy – Flyer</title>
<link rel="stylesheet" href="https://fonts.googleapis.com/css2?family=Exo+2:wght@500;600;700&family=Questrial&display=swap">
<style>
:root{
  --plum:#4e2a4c;
  --plum-text:#5b2d57;
  --green:#3cb043;
  --panel:#d4d4d6;
  --ink:#3a3a3a;
  --paper:#ffffff;
  --paper-shade:#efefef;
  --sky-top:#c98fc2;
  --sky-mid:#f0b3c2;
  --sky-glow:#f58a3a;
  --sun:#fbd23c;
  --ground:#2a1710;
}
*{box-sizing:border-box;margin:0;padding:0}
html,body{width:884px;height:1200px;overflow:hidden;background:#fff}
body{font-family:"Questrial",sans-serif;color:var(--ink)}
.flyer{position:relative;width:884px;height:1200px;background:linear-gradient(#fff 0,var(--paper-shade) 50%,#fff 100%);overflow:hidden}

.hero{position:absolute;left:0;top:0;width:884px;height:330px}
.brand{position:absolute;left:620px;top:40px;width:228px;height:144px;border-radius:50%;background:#fff;display:flex;align-items:center;justify-content:center;text-align:center}
.brand-name{font-family:"Questrial",sans-serif;color:var(--plum-text);font-size:17px;line-height:19px;letter-spacing:.5px}

.needs{position:absolute;left:37px;top:346px;width:807px;display:grid;grid-template-columns:392px 400px;column-gap:15px;row-gap:15px}
.need{background:var(--panel);border-radius:8px;height:126px;text-align:center;padding-top:20px}
.need h2{font-family:"Exo 2",sans-serif;font-weight:600;font-size:20px;color:var(--plum-text);margin-bottom:9px}
.need p{font-size:12px;line-height:15px;color:#444}
.need.short p{line-height:16.5px}

.headline{position:absolute;left:0;width:884px;top:640px;text-align:center;font-family:"Exo 2",sans-serif;font-weight:600;font-size:28px;color:var(--plum-text)}

.about{position:absolute;left:59px;top:695px;width:533px;font-size:11.6px;line-height:13.8px;text-align:justify;color:#333}
.about p{margin-bottom:13px}
.portrait{float:left;width:145px;height:203px;margin:0 20px 6px 0;border-radius:6px;background:linear-gradient(160deg,#e8e6e4 0%,#d8cfc8 45%,#c0494b 70%,#9a3d44 100%)}

.credentials{position:absolute;left:606px;top:695px;width:236px;height:284px;border-radius:8px;background:var(--plum);color:#e9dfe9;padding:18px 16px}
.credentials h3{font-family:"Exo 2",sans-serif;font-weight:500;font-size:14px;color:#fff;margin-bottom:14px}
.credentials ul{list-style:none;font-style:italic;font-size:11.4px;line-height:13px}
.credentials h4{font-family:"Questrial",sans-serif;font-weight:400;font-size:11.4px;color:#fff;margin-top:12px}
.credentials .assurance{font-size:11.4px;line-height:13px;margin-top:34px}

.footer{position:absolute;left:0;top:1040px;width:884px;height:160px}
.contact{position:absolute;color:#fff;font-family:"Exo 2",sans-serif;font-weight:600}
.address{left:32px;top:1143px;font-size:12.5px;line-height:15px;display:flex;gap:5px}
.address .lines{display:block}
.phone{left:336px;top:1151px;font-size:23px;display:flex;align-items:center;gap:4px}
.online{left:523px;top:1143px;font-size:12.5px;line-height:18px}
.online div{display:flex;align-items:center;gap:5px}
.social{position:absolute;top:1153px;left:774px;display:flex;gap:6px}
.social span{width:20px;height:20px;border-radius:3px;background:#3b79c9;display:block}
</style>
</head>
<body>
<main class="flyer">

  <svg class="hero" viewBox="0 0 884 330" role="img" aria-label="Photograph: family silhouettes running across a hilltop against a sunset sky">
    <defs>
      <linearGradient id="sky" x1="0" y1="0" x2="0" y2="1">
        <stop offset="0" stop-color="var(--sky-top)"/>
        <stop offset=".35" stop-color="var(--sky-mid)"/>
        <stop offset=".62" stop-color="var(--sky-glow)"/>
        <stop offset=".76" stop-color="var(--sun)"/>
        <stop offset=".84" stop-color="#7a3a1c"/>
        <stop offset="1" stop-color="var(--ground)"/>
      </linearGradient>
    </defs>
    <rect width="884" height="330" fill="url(#sky)"/>
    <path d="M0 296 Q420 335 884 250 L884 330 L0 330 Z" fill="#fff"/>
    <path d="M0 299 Q420 338 884 256" fill="none" stroke="var(--green)" stroke-width="5"/>
  </svg>

  <div class="brand"><div class="brand-name">LARKMORE<br>COUNSELLING &amp;<br>HYPNOTHERAPY</div></div>

  <section class="needs">
    <article class="need">
      <h2>Clarify</h2>
      <p>I want to understand more about my relationship with others.<br>I'm not sure how to cope with my grief and loss.<br>I feel anxious and scared and I'm not sure why.<br>I'm not sure how to relax.</p>
    </article>
    <article class="need">
      <h2>Growth and development</h2>
      <p>I want to improve my level of confidence and self esteem.<br>I want to personally gain a greater self awareness.<br>I want to improve communication with my manager and my team.<br>I want to move on to something else.</p>
    </article>
    <article class="need">
      <h2>Explore</h2>
      <p>There's something I want to explore and make sense of.<br>I'm feeling really down, low and depressed and I feel stuck.<br>To me the world just looks like a fog.<br>I'd like to have some support and somebody to listen.<br>I feel overwhelmed.</p>
    </article>
    <article class="need short">
      <h2>Behaviour change</h2>
      <p>I want to stop smoking.<br>I want to feel less anxious.<br>I want to stop harming myself.<br>I want to stop the phobia I have.</p>
    </article>
  </section>

  <h1 class="headline">Trusted Professional An approach tailored to you</h1>

  <section class="about">
    <div class="portrait" role="img" aria-label="Photograph: portrait of the counsellor seated in a chair"></div>
    <p>There are times in all of our lives when we feel we have lost our way, we need a listening ear or we simply want somebody to work together with to help us reach the next step in our journey, whatever that may be. Maybe that sounds like you and you're looking for somebody to help you take that first step or maybe you simply want somebody to share your concerns with and really feel heard.</p>
    <p>I am a fully qualified counsellor and I'm able to provide a safe, confidential environment for you to speak, to feel, to be heard and valued as an individual in what can be a scary and challenging world.</p>
    <p>I have experience of working with people with a wide range of concerns. Some examples include loss and grief, depression, anxiety, relationships, self-esteem, eating disorders, confidence, general personal development and growth. I find this work really rewarding and it's been a privilege to work with all of these people.</p>
    <p>My main way of working is based on the Transactional Analysis model and I also able to use a wide range of techniques and theories, tailoring my approach to suit you. Some examples include NLP, CBT, EFT, Mindfulness, creative sand-tray.</p>
    <p>In addition to a more typical counselling role, I am able to offer hypnotherapy. I find this works really well in combination with counselling. I am also happy to offer this on its own for specific things such as giving up smoking, phobias, relaxation, confidence and much more.</p>
    <p>I'm happy to support individuals over fourteen years of age and couples on a face-to-face basis for short, medium or long term therapy.</p>
  </section>

  <aside class="credentials">
    <h3>Qualifications &amp; Memberships</h3>
    <ul>
      <li>Diploma in Counselling</li>
      <li>Diploma in Hypnotherapy</li>
      <li>Diploma in Management</li>
      <li>Diploma in NLP</li>
      <li>BA (Hons) Education and Research</li>
    </ul>
    <h4>Member of:</h4>
    <ul>
      <li>ACPR (Member)</li>
      <li>TAAU (Member)</li>
      <li>Guild of Talking Therapists</li>
      <li>Hypnotherapy Practitioners Circle (Member)</li>
    </ul>
    <p class="assurance">Fully insured and CRB checked.<br>Data Protection Registered.</p>
  </aside>

  <svg class="footer" viewBox="0 0 884 160" aria-hidden="true">
    <path d="M0 58 Q430 70 884 10 L884 160 L0 160 Z" fill="var(--plum)"/>
    <path d="M0 50 Q430 62 884 2" fill="none" stroke="var(--green)" stroke-width="5"/>
  </svg>

  <div class="contact address">
    <svg width="10" height="14" viewBox="0 0 10 14" aria-hidden="true"><path d="M5 0a5 5 0 0 0-5 5c0 4 5 9 5 9s5-5 5-9a5 5 0 0 0-5-5zm0 7a2 2 0 1 1 0-4 2 2 0 0 1 0 4z" fill="#fff"/></svg>
    <span class="lines">Larkmore Counselling &amp; Hypnotherapy,<br>14C, Mill Row, Harrowby<br>East Downs HB4 2QL</span>
  </div>

  <div class="contact phone">
    <svg width="18" height="18" viewBox="0 0 18 18" aria-hidden="true"><circle cx="9" cy="9" r="8" fill="none" stroke="#fff" stroke-width="1.4"/><path d="M6.2 4.5l1.6 2.2-1 1.2c.6 1.3 1.5 2.2 2.6 2.8l1.2-1 2.1 1.6-1 1.8c-3.4-.3-6.3-3.3-6.5-6.8z" fill="#fff"/></svg>
    07700 900418
  </div>

  <div class="contact online">
    <div><svg width="12" height="9" viewBox="0 0 12 9" aria-hidden="true"><rect x=".5" y=".5" width="11" height="8" fill="none" stroke="#fff"/><path d="M.5.5L6 5l5.5-4.5" fill="none" stroke="#fff"/></svg>larkmoretherapy@mailvale.com</div>
    <div><svg width="12" height="12" viewBox="0 0 12 12" aria-hidden="true"><circle cx="6" cy="6" r="5.3" fill="none" stroke="#fff"/><ellipse cx="6" cy="6" rx="2.3" ry="5.3" fill="none" stroke="#fff"/><path d="M.7 6h10.6" stroke="#fff"/></svg>larkmoretherapy.plumweave.com</div>
  </div>

  <div class="social" aria-hidden="true"><span></span><span></span></div>

</main>
</body>
</html>
```